Pelmora Business Cards

Create new business cards with the details below.

Gregor Tash
Director

MB: +61 415 230 964
PH: 1300 517 493
Email: gregor.tash@pelmora.com.au
Address: 27C Harlow Lane, Thornbrook VIC 3187 Australia
Website: www.pelmora.com.au

Target Market(s)

Other business

Industry/Entity Type

Business

Requirements
Must have
• must be clean looking

```html
<!DOCTYPE html>
<html lang="en">
<head>
<meta charset="utf-8">
<title>Pelmora Business Cards</title>
<link rel="stylesheet" href="https://fonts.googleapis.com/css2?family=Open+Sans:wght@400;700&display=swap">
<style>
  :root {
    --backdrop: #3a322d;
    --card: #161616;
    --card-edge: #222;
    --lime: #8cc63f;
    --white: #f2f2f2;
    --muted: #cfcfcf;
    --silver: #7d7d7d;
    --divider: #555;
  }
  * { margin: 0; padding: 0; box-sizing: border-box; }
  html, body { width: 1200px; height: 827px; overflow: hidden; }
  body {
    background: var(--backdrop);
    font-family: "Open Sans", Arial, sans-serif;
    position: relative;
  }
  .card {
    position: absolute;
    top: 255px;
    width: 520px;
    height: 318px;
    background: var(--card);
    border: 1px solid var(--card-edge);
    box-shadow: 0 10px 30px rgba(0,0,0,.45);
  }
  .card--front { left: 50px; }
  .card--back { left: 630px; }

  .brand { display: flex; align-items: center; gap: 10px; }
  .brand__square { width: 26px; height: 26px; }
  .brand__name { font-weight: 700; letter-spacing: 1px; line-height: 1; }

  .card--front .brand {
    position: absolute; inset: 0; justify-content: center;
  }
  .card--front .brand__square { width: 44px; height: 44px; background: var(--silver); }
  .card--front .brand__name { font-size: 52px; color: var(--silver); }

  .card--back .brand { position: absolute; left: 30px; top: 118px; }
  .card--back .brand__square { background: var(--lime); }
  .card--back .brand__name { font-size: 30px; color: var(--white); }

  .divider {
    position: absolute; left: 240px; top: 100px; width: 1px; height: 78px;
    background: var(--divider);
  }
  .contact { position: absolute; left: 262px; top: 62px; }
  .contact__name { font-size: 22px; font-weight: 700; color: var(--lime); line-height: 1.1; }
  .contact__role { font-size: 12px; color: var(--muted); margin-bottom: 12px; }
  .contact__address { font-size: 12.5px; color: var(--white); line-height: 1.4; margin-bottom: 10px; }
  .contact__list { list-style: none; }
  .contact__item {
    display: flex; align-items: center; gap: 8px;
    font-size: 12.5px; color: var(--white); line-height: 1.55;
  }
  .contact__icon { width: 11px; height: 11px; flex: none; }
</style>
</head>
<body>
  <section class="card card--front">
    <div class="brand">
      <span class="brand__square"></span>
      <span class="brand__name">PELMORA</span>
    </div>
  </section>

  <section class="card card--back">
    <div class="brand">
      <span class="brand__square"></span>
      <span class="brand__name">PELMORA</span>
    </div>
    <div class="divider"></div>
    <div class="contact">
      <p class="contact__name">Gregor Tash</p>
      <p class="contact__role">Director</p>
      <p class="contact__address">27C Harlow Lane,<br>Thornbrook VIC 3187 Australia</p>
      <ul class="contact__list">
        <li class="contact__item">
          <svg class="contact__icon" viewBox="0 0 12 12"><path fill="#8cc63f" d="M2.5 0.5l2 2.5-1 1.2a7 7 0 0 0 4.3 4.3l1.2-1 2.5 2-1.3 1.8C5 11 1 7 0.7 1.8z"/></svg>
          1300 517 493
        </li>
        <li class="contact__item">
          <svg class="contact__icon" viewBox="0 0 12 12"><rect x="3" y="0.5" width="6" height="11" rx="1" fill="none" stroke="#8cc63f" stroke-width="1.2"/><circle cx="6" cy="9.5" r="0.7" fill="#8cc63f"/></svg>
          +61 415 230 964
        </li>
        <li class="contact__item">
          <svg class="contact__icon" viewBox="0 0 12 12"><rect x="0.5" y="2" width="11" height="8" fill="#8cc63f"/><path d="M0.5 2l5.5 4.5L11.5 2" fill="none" stroke="#161616" stroke-width="1"/></svg>
          gregor.tash@pelmora.com.au
        </li>
        <li class="contact__item">
          <svg class="contact__icon" viewBox="0 0 12 12"><circle cx="6" cy="6" r="5.5" fill="#8cc63f"/><path d="M0.5 6h11M6 0.5c-3 3-3 8 0 11M6 0.5c3 3 3 8 0 11" fill="none" stroke="#161616" stroke-width="0.8"/></svg>
          www.pelmora.com.au
        </li>
      </ul>
    </div>
  </section>
</body>
</html>
```